CD cover - Horizons: Ample Room To Share

Welcome!

The album contains acoustic music with positive and affirmative lyrics.

Here's a medley of some songs.
https://files.wavecrate-example.net/u/83610457/bela_morvik_ample_room_to_share_20150220.mp3

This music and life style is about enjoying ourselves and this game we call life. Respect, gratitude, love, forgiveness, simplicity, together these lead to a happy, blissful life. If the potential listener - when looking at the cover - gets this message, than it's perfect. Just make it simple, playful, beautiful. :)

BUT PLEASE AVOID CLICHÉS!! Come up with something original! Thank you!

Note: the front cover in case of online purchase of the album will be shown on a cell-phone for example. If the image is complicated and too detailed, it won't look like something.

The CD cover project has 4 parts:
1. CD cover front outside
2. CD cover front inside (track list)
3. CD cover back
4. CD (print on the disc)

The performer: Bela Morvik (logo attached). Please use the logo with the original colors and design the cover to go well with it.

Album title: Horizons: Ample Room To Share
All my upcoming albums are going to be called "Horizons: something"

Track list:
1. Warm (3:49)
2. Hope For Many (3:48)
3. We Will Rise (4:36)
4. Sunny Road (2:54)
5. Letting Go (2:58)
6. Weightless (3:41)
7. Wonderful (3:23)
8. Thankful Heart (4:03)
9. Calm & Kindness (3:39)
10. Quiet Harbor (4:03)
11. Softly Now (4:38)
12. Open Skies (4:17)

All songs written by Bela Morvik
Copyright Belasound 2015.
www.belasound-example.net

I am going to need the cover in RGB format.

That's pretty much it. If I missed something important, mail me without hesitation! Enjoy! :)

Target Market(s)

New Age spiritual people, positive thinking people.

Industry/Entity Type

Cell Phone

Requirements
Must have
• Easy to read text and logo. I'm still building the brand.
Nice to have
• Light colors
Should not have
• Any kind of negativity at all.

```html
<!DOCTYPE html>
<html lang="en">
<head>
<meta charset="utf-8">
<title>Horizons: Ample Room To Share — CD Cover</title>
<link rel="stylesheet" href="https://fonts.googleapis.com/css2?family=Archivo+Black&family=Raleway:wght@300;400&family=Arimo:wght@700&display=swap">
<style>
  :root {
    --page: #f1f1f1;
    --paper: #ffffff;
    --orange: #f6a823;
    --ink: #3b3b3b;
    --sky: #fbe68a;
    --sun: #f7c42b;
    --meadow: #93c83c;
    --grass: #3f8a1d;
  }
  * { box-sizing: border-box; margin: 0; padding: 0; }
  html, body { width: 1200px; height: 634px; overflow: hidden; background: var(--page); }
  .spread { position: relative; width: 1200px; height: 634px; }
  .panel {
    position: absolute; top: 42px; width: 538px; height: 539px;
    background: var(--paper); overflow: hidden;
  }
  .panel--inside { left: 61px; }
  .panel--front { left: 605px; }
  .panel .artwork { position: absolute; inset: 0; width: 100%; height: 100%; }

  .tracklist {
    position: absolute; top: 74px; left: 292px; list-style: none;
    font-family: "Raleway", sans-serif; font-weight: 300;
    font-size: 12.5px; line-height: 22.2px; color: var(--orange);
  }
  .tracklist li:nth-child(1)  { margin-left: 0; }
  .tracklist li:nth-child(2)  { margin-left: 3px; }
  .tracklist li:nth-child(3)  { margin-left: 6px; }
  .tracklist li:nth-child(4)  { margin-left: 9px; }
  .tracklist li:nth-child(5)  { margin-left: 12px; }
  .tracklist li:nth-child(6)  { margin-left: 15px; }
  .tracklist li:nth-child(7)  { margin-left: 18px; }
  .tracklist li:nth-child(8)  { margin-left: 21px; }
  .tracklist li:nth-child(9)  { margin-left: 24px; }
  .tracklist li:nth-child(10) { margin-left: 27px; }
  .tracklist li:nth-child(11) { margin-left: 30px; }
  .tracklist li:nth-child(12) { margin-left: 33px; }

  .credits {
    position: absolute; left: 27px; bottom: 20px;
    font-family: "Arimo", sans-serif; font-weight: 700;
    font-size: 10.5px; line-height: 12px; color: var(--orange);
  }

  .artist-name {
    position: absolute; display: flex; align-items: center;
    font-family: "Raleway", sans-serif; font-weight: 400; color: var(--ink);
    white-space: nowrap;
  }
  .artist-name .dot { border-radius: 50%; background: var(--orange); flex: none; }
  .artist-name--small { right: 18px; bottom: 22px; font-size: 11px; gap: 5px; }
  .artist-name--small .dot { width: 14px; height: 14px; }
  .artist-name--large { left: 268px; top: 52px; font-size: 30px; gap: 12px; }
  .artist-name--large .dot { width: 34px; height: 34px; }

  .album-title {
    position: absolute; left: 160px; top: 262px;
    transform: rotate(-9deg); transform-origin: left top;
    font-family: "Archivo Black", sans-serif; color: var(--orange);
    text-transform: uppercase; line-height: 0.92;
  }
  .album-title .series { display: block; font-size: 30px; }
  .album-title .name { display: block; font-size: 46px; }
</style>
</head>
<body>
<main class="spread">

  <section class="panel panel--inside" aria-label="Inside cover with track list">
    <svg class="artwork" viewBox="0 0 553 554" preserveAspectRatio="none">
      <defs>
        <linearGradient id="meadow-inside" x1="0" y1="0" x2="0" y2="1">
          <stop offset="0" stop-color="var(--sun)"/>
          <stop offset="0.22" stop-color="var(--sky)"/>
          <stop offset="0.4" stop-color="var(--meadow)"/>
          <stop offset="1" stop-color="var(--grass)"/>
        </linearGradient>
      </defs>
      <rect width="553" height="554" fill="url(#meadow-inside)" role="img" aria-label="Sunlit green meadow with wildflowers under a golden sky"/>
      <polygon fill="var(--paper)" points="0,0 85,0 115,295 0,135"/>
      <polygon fill="var(--paper)" points="70,554 165,554 118,390"/>
      <polygon fill="var(--paper)" points="185,554 272,554 237,257"/>
      <polygon fill="var(--paper)" points="287,0 553,0 553,554 367,554"/>
    </svg>

    <ol class="tracklist">
      <li>1. Warm (3:49)</li>
      <li>2. Hope For Many (3:48)</li>
      <li>3. We Will Rise (4:36)</li>
      <li>4. Sunny Road (2:54)</li>
      <li>5. Letting Go (2:58)</li>
      <li>6. Weightless (3:41)</li>
      <li>7. Wonderful (3:23)</li>
      <li>8. Thankful Heart (4:03)</li>
      <li>9. Calm &amp; Kindness (3:39)</li>
      <li>10. Quiet Harbor (4:03)</li>
      <li>11. Softly Now (4:38)</li>
      <li>12. Open Skies (4:17)</li>
    </ol>

    <p class="credits">All songs written by Bela Morvik<br>Copyright Belasound 2015.<br>www.belasound-example.net</p>

    <div class="artist-name artist-name--small"><span class="dot"></span>Bela Morvik</div>
  </section>

  <section class="panel panel--front" aria-label="Front cover">
    <svg class="artwork" viewBox="0 0 553 554" preserveAspectRatio="none">
      <defs>
        <linearGradient id="meadow-front" x1="0" y1="0" x2="0" y2="1">
          <stop offset="0" stop-color="var(--sun)"/>
          <stop offset="0.22" stop-color="var(--sky)"/>
          <stop offset="0.4" stop-color="var(--meadow)"/>
          <stop offset="1" stop-color="var(--grass)"/>
        </linearGradient>
      </defs>
      <polygon fill="url(#meadow-front)" points="0,0 233,0 275,554 0,554" role="img" aria-label="Meadow stretching to a bright sunrise on the horizon"/>
      <polygon fill="var(--paper)" points="88,554 118,554 213,172"/>
      <polygon fill="var(--paper)" points="0,292 0,308 100,554 116,554"/>
    </svg>

    <div class="artist-name artist-name--large"><span class="dot"></span>Bela Morvik</div>

    <h1 class="album-title">
      <span class="series">Horizons:</span>
      <span class="name">Ample</span>
      <span class="name">Room To</span>
      <span class="name">Share</span>
    </h1>
  </section>

</main>
</body>
</html>
```